IT Company Business Card design

Brisk Node is a new computer solutions business focusing on setting up servers and computer systems for small to medium sized businesses.

A business client will either request a solution, or support for a current system and we will turn up on site to provide these services.

We are bast in Christchurch, New Zealand.

We are looking for unique business card's that stand out and show off the business in a professional light.

Open to all idea's etc.

Industry/Entity Type

Computer

Requirements
Must have
• Business Logo (AI file attached)
Employee Name
Business title
Business landline number
Cell phone number
Email
Web URL
Nice to have
• Could be nice to have some keywords (possibly on the back) such as:

Business IT solutions
Network installations
Phone solutions
Server management
Software diagnostics

The above is not needed, just an idea.

```html
<!DOCTYPE html>
<html lang="en">
<head>
<meta charset="utf-8">
<title>Brisk Node – Business Card</title>
<link rel="stylesheet" href="https://fonts.googleapis.com/css2?family=Montserrat:wght@400&family=Open+Sans:wght@400&family=Tinos&display=swap">
<style>
  :root {
    --page-bg: #e9e6e1;
    --card-bg: #fbfcfd;
    --card-tint: #eef6fb;
    --ink-dark: #1d1f24;
    --ink-blue: #4a78c8;
    --ink-navy: #2b3d8f;
    --ink-soft: #6a7bb0;
    --mark-blue: #1f86c6;
    --divider: #9fb3c8;
  }
  * { margin: 0; padding: 0; box-sizing: border-box; }
  html, body { width: 1200px; height: 1000px; overflow: hidden; }
  body {
    background: var(--page-bg);
    position: relative;
  }
  .business-card {
    position: absolute;
    left: 180px;
    top: 250px;
    width: 840px;
    height: 480px;
    background: linear-gradient(135deg, var(--card-bg) 0%, var(--card-tint) 100%);
    box-shadow: 0 10px 30px rgba(0,0,0,0.18);
  }
  .brand {
    position: absolute;
    left: 150px;
    top: 92px;
    display: flex;
    align-items: center;
    gap: 26px;
  }
  .brand-dot {
    width: 100px;
    height: 100px;
    border-radius: 50%;
    background: var(--mark-blue);
  }
  .brand-name {
    font-family: "Montserrat", sans-serif;
    font-weight: 400;
    font-size: 40px;
    letter-spacing: 4px;
    color: var(--ink-dark);
    text-transform: uppercase;
    line-height: 1;
  }
  .brand-tagline {
    font-family: "Open Sans", sans-serif;
    font-size: 30px;
    color: var(--ink-blue);
    margin-top: 8px;
    line-height: 1;
  }
  .contacts {
    position: absolute;
    left: 0;
    top: 222px;
    width: 100%;
    font-family: "Tinos", serif;
    font-size: 19px;
    color: var(--ink-navy);
  }
  .contacts-divider {
    position: absolute;
    left: 420px;
    top: 0;
    width: 1px;
    height: 160px;
    background: var(--divider);
  }
  .contact-line {
    position: absolute;
    display: flex;
    align-items: center;
    gap: 8px;
    white-space: nowrap;
    line-height: 1.2;
  }
  .contact-line svg { flex: none; }
  .col-left { right: 432px; text-align: right; }
  .col-right { left: 432px; }
  .employee-title {
    font-size: 15px;
    color: var(--ink-soft);
    font-style: italic;
  }
</style>
</head>
<body>
  <main class="business-card">
    <div class="brand">
      <div class="brand-dot"></div>
      <div class="brand-text">
        <div class="brand-name">Brisk Node</div>
        <div class="brand-tagline">Computer Solutions</div>
      </div>
    </div>

    <section class="contacts">
      <div class="contacts-divider"></div>

      <div class="contact-line col-left" style="top:2px">Mr.EmployeeName</div>
      <div class="contact-line col-left employee-title" style="top:28px">Systems Engineer</div>
      <div class="contact-line col-left" style="top:72px">
        <svg width="11" height="18" viewBox="0 0 11 18" aria-hidden="true"><rect x="1" y="1" width="9" height="16" rx="2" fill="var(--ink-navy)"/><rect x="2.5" y="3" width="6" height="6" fill="#fff"/></svg>
        03 555 0142
      </div>
      <div class="contact-line col-left" style="top:118px">
        <svg width="17" height="12" viewBox="0 0 17 12" aria-hidden="true"><rect x="0.5" y="0.5" width="16" height="11" fill="var(--ink-navy)"/><path d="M1 1 L8.5 7 L16 1" fill="none" stroke="#fff" stroke-width="1.3"/></svg>
        employee@brisknode.com
      </div>

      <div class="contact-line col-right" style="top:40px">
        <svg width="17" height="17" viewBox="0 0 17 17" aria-hidden="true"><rect x="0" y="0" width="17" height="17" rx="3" fill="var(--ink-navy)"/><path d="M5 3.5 C4 4.5 4 7 6.5 10 C9 13 11.5 13.5 12.8 12.3 L11 10.3 L9.8 11 C8.5 10.3 6.8 8.5 6.3 7.2 L7 6 Z" fill="#fff"/></svg>
        03 555 0142
      </div>
      <div class="contact-line col-right" style="top:94px">
        <svg width="20" height="20" viewBox="0 0 20 20" aria-hidden="true"><circle cx="10" cy="10" r="8.5" fill="none" stroke="var(--ink-navy)" stroke-width="2"/><ellipse cx="10" cy="10" rx="3.5" ry="8.5" fill="none" stroke="var(--ink-navy)" stroke-width="1.3"/><line x1="1.5" y1="10" x2="18.5" y2="10" stroke="var(--ink-navy)" stroke-width="1.3"/></svg>
        www.brisknode.com
      </div>
    </section>
  </main>
</body>
</html>
```